Law Firm Website

Our client has never had a website, but their services are similar to: https://www.tallbrook-vance.com.

They are a personal injury attorney, husband, and wife team.

Coding

Coded - Design and coding required

Number of Pages Required

1 page

Font styles to use
Sans Serif

Colors
0054AA
0677BA
7BADD7
CADEEF
E8F1F8

```html
<!DOCTYPE html>
<html lang="en">
<head>
<meta charset="utf-8">
<title>Northgate Law</title>
<link rel="stylesheet" href="https://fonts.googleapis.com/css2?family=Montserrat:ital,wght@0,400;0,500;0,600;0,700;1,400&display=swap">
<style>
:root{
  --blue-deep:#0054AA;
  --blue:#0b63c9;
  --blue-mid:#0677BA;
  --blue-bright:#1d9bf0;
  --blue-soft:#7BADD7;
  --blue-pale:#CADEEF;
  --blue-mist:#E8F1F8;
  --ink:#1c2733;
  --white:#ffffff;
}
*{box-sizing:border-box;margin:0;padding:0}
html,body{width:1200px;height:4474px;overflow:hidden}
body{position:relative;background:var(--white);font-family:"Montserrat",sans-serif;color:var(--ink)}
.abs{position:absolute}
.layer{position:absolute;left:0;top:0;width:1200px;height:4474px}

.site-header{position:absolute;left:0;top:0;width:1200px;height:63px;background:var(--blue);z-index:5}
.brand-tab{position:absolute;left:148px;top:0;width:230px;height:130px;background:var(--white);clip-path:polygon(0 0,100% 0,100% 78%,50% 100%,0 78%);z-index:6;display:flex;align-items:center;justify-content:center;padding-bottom:26px}
.brand-name{font-weight:700;color:var(--blue);font-size:19px;letter-spacing:2px;white-space:nowrap}
.main-nav{position:absolute;right:150px;top:0;height:63px;display:flex;gap:32px;align-items:center;z-index:6}
.main-nav a{color:var(--white);text-decoration:none;font-size:14px;font-weight:500}
.main-nav a.active{font-weight:700}

.hero-photo{position:absolute;left:0;top:63px;width:1200px;height:740px;background:linear-gradient(120deg,#c9c4bd 0%,#8d96a3 35%,#4d5a6c 60%,#b8b2aa 100%)}
.hero-panel{position:absolute;left:148px;top:238px;width:900px;height:347px;background:rgba(40,110,210,.45)}
.hero-title{position:absolute;left:0;top:290px;width:1200px;text-align:center;color:var(--white);font-weight:700;font-size:56px;line-height:68px;text-shadow:0 2px 6px rgba(0,0,0,.35)}
.btn{display:inline-flex;align-items:center;justify-content:center;background:var(--blue-bright);color:var(--white);font-weight:700;border-radius:24px;text-decoration:none;font-size:18px}
.hero-btn{position:absolute;left:503px;top:465px;width:190px;height:46px}

.heading{font-weight:700;color:var(--blue);letter-spacing:.5px}
.rule{display:flex;gap:30px;margin-top:10px}
.rule span{height:3px;background:var(--blue);width:110px}
.rule.light span{background:var(--white)}
.copy{font-size:11px;line-height:16px;color:#222}

.about{position:absolute;left:150px;top:832px;width:545px}
.about .heading{font-size:44px}
.about .copy{margin-top:30px}
.about .btn{margin-top:40px;width:172px;height:46px}
.about-photo{position:absolute;left:710px;top:845px;width:480px;height:460px;background:linear-gradient(180deg,#2a3442 0%,#1b2330 100%);clip-path:polygon(12% 12%,60% 0,100% 8%,100% 100%,0 100%,4% 40%)}

.practice-head{position:absolute;left:0;top:1270px;width:1200px;text-align:center;color:var(--white)}
.practice-head h2{font-size:44px;font-weight:700}
.practice-head .rule{justify-content:center;gap:300px}
.practice-head .rule span{width:230px}
.practice-head p{margin:22px auto 0;width:580px;font-size:12px;line-height:19px}
.area-label{position:absolute;width:200px;text-align:center;color:var(--white);font-weight:700;font-size:22px;line-height:26px;text-shadow:0 1px 4px rgba(0,0,0,.5)}

.comp-photo{position:absolute;left:0;top:2024px;width:590px;height:756px;background:linear-gradient(135deg,#e9e6e0 0%,#cfc9c0 45%,#7d858f 100%);clip-path:polygon(0 0,100% 18%,100% 85%,0 100%)}
.comp{position:absolute;left:650px;top:2195px;width:410px}
.comp .heading{font-size:38px;line-height:46px}
.comp .rule{gap:65px}
.comp .rule span{width:145px}
.comp .copy{margin-top:50px;font-size:12px;line-height:19px}
.comp .btn{margin-top:30px;width:172px;height:46px}

.clients{position:absolute;left:0;top:2850px;width:1200px;text-align:center;color:var(--white)}
.clients h2{font-size:44px;font-weight:700}
.quote-text{margin:30px auto 0;width:860px;font-style:italic;font-size:14px;line-height:21px}
.client-name{position:absolute;left:0;top:3298px;width:1200px;text-align:center;color:var(--white);font-weight:600;font-size:17px}
.client-role{position:absolute;left:0;top:3325px;width:1200px;text-align:center;color:var(--white);font-size:14px}
.dots{position:absolute;left:552px;top:3375px;display:flex;gap:8px}
.dots span{width:14px;height:14px;border-radius:50%;background:var(--white)}

.contact{position:absolute;left:150px;top:3560px}
.contact .heading{font-size:40px}
.contact .rule{gap:35px}
.field{position:absolute;border:1px solid #bfc6cf;background:var(--white);font-size:10px;color:#999;padding:8px 9px;font-family:inherit}
.submit{position:absolute;left:150px;top:3890px;width:130px;height:42px;font-size:18px}

.touch{position:absolute;left:688px;top:3510px;width:512px;height:460px;background:linear-gradient(90deg,#3b3f45 0%,#55595f 100%)}
.touch-photo{position:absolute;left:232px;top:0;width:280px;height:460px;background:linear-gradient(180deg,#6b6e72 0%,#2b3140 100%);opacity:.9}
.touch h2{position:absolute;left:57px;top:48px;font-size:36px;color:var(--white);font-weight:700}
.touch .rule{position:absolute;left:57px;top:100px;gap:35px}
.touch .rule span{width:115px}
.contact-item{position:absolute;left:57px;display:flex;gap:18px;color:var(--white)}
.contact-item .icon{width:34px;height:34px;border-radius:50%;background:var(--white);display:flex;align-items:center;justify-content:center;flex:none}
.contact-item b{display:block;font-size:19px;font-weight:600}
.contact-item small{display:block;font-size:12px;line-height:17px;margin-top:6px}

.footer-name{position:absolute;left:0;top:4150px;width:1200px;text-align:center;color:var(--white);font-weight:600;font-size:36px;letter-spacing:6px}
.footer-nav{position:absolute;left:0;top:4268px;width:1200px;display:flex;justify-content:center;gap:42px}
.footer-nav a{color:var(--white);text-decoration:none;font-size:15px}
.social{position:absolute;left:533px;top:4330px;display:flex;gap:14px}
.social span{width:34px;height:34px;border-radius:50%;border:2px solid var(--white);background:var(--blue-bright)}
.copyright{position:absolute;left:0;top:4428px;width:1200px;text-align:center;color:var(--white);font-size:11px}
</style>
</head>
<body>

<header class="site-header">
  <nav class="main-nav">
    <a class="active" href="#">Home</a><a href="#">Our Firm</a><a href="#">Practice Areas</a><a href="#">Testimonials</a><a href="#">Blog</a><a href="#">Contact</a>
  </nav>
</header>
<div class="brand-tab"><span class="brand-name">NORTHGATE LAW</span></div>

<div class="hero-photo" role="img" aria-label="Lawyer reviewing documents with a client in an office"></div>
<div class="hero-panel"></div>
<h1 class="hero-title">WE ARE HERE TO<br>PROTECT YOU</h1>
<a class="btn hero-btn" href="#">CONTACT US</a>

<svg class="layer" viewBox="0 0 1200 4474" aria-hidden="true">
  <defs>
    <linearGradient id="bandBlue" x1="0" y1="0" x2="0" y2="1">
      <stop offset="0" stop-color="#0d63cc"/><stop offset="1" stop-color="#0a55b8"/>
    </linearGradient>
    <linearGradient id="brightBlue" x1="0" y1="0" x2="1" y2="1">
      <stop offset="0" stop-color="#1d9bf0"/><stop offset="1" stop-color="#1a83e0"/>
    </linearGradient>
  </defs>
  <!-- about backdrop -->
  <polygon points="0,630 620,795 1200,795 1200,1320 0,1320" fill="#f5f6f7"/>
  <polygon points="620,795 1200,625 1200,1300 960,1250" fill="url(#brightBlue)"/>
  <polygon points="0,1140 0,1320 1200,1320 1200,1140" fill="#ffffff" opacity="0"/>
  <!-- practice band -->
  <polygon points="0,1300 600,1150 1200,1300 1200,1945 600,2090 0,1945" fill="url(#brightBlue)"/>
  <polygon points="0,1318 600,1168 1200,1318 1200,1928 600,2072 0,1928" fill="url(#bandBlue)"/>
  <!-- clients band -->
  <polygon points="0,2860 600,2748 1200,2860 1200,3326 600,3448 0,3326" fill="url(#bandBlue)"/>
  <polygon points="0,2860 600,2748 1200,2860 1200,2876 600,2764 0,2876" fill="url(#brightBlue)"/>
  <!-- footer -->
  <polygon points="0,4200 600,4028 1200,4200 1200,4474 0,4474" fill="url(#bandBlue)"/>
</svg>

<div class="about-photo" role="img" aria-label="Husband and wife attorney team standing in business suits"></div>
<section class="about">
  <h2 class="heading">ABOUT US</h2>
  <div class="rule"><span></span><span></span></div>
  <p class="copy">Lorem ipsum dolor sit amet, consectetur adipiscing elit, sed do eiusmod tempor incididunt ut labore et dolore magna aliqua. Ut enim ad minim veniam, quis nostrud exercitation ullamco laboris nisi ut aliquip ex ea commodo consequat. Duis aute irure dolor in reprehenderit in voluptate velit esse cillum dolore eu fugiat nulla pariatur. Excepteur sint occaecat cupidatat non proident, sunt in culpa qui officia deserunt mollit anim id est Sed ut pm, totam rem aperiam, eaque ipsa quae ab illovitae dicta sunt explicabo. Duis aute irure dolor in reprehenderit in voluptate velit esse cillum dolore eu fugiat nulla pariatur. Excepteur sint occaecat cupidatat non proident, sunt in culpa qui officia deserunt mollit anim id est laborum.</p>
  <a class="btn" href="#">READ MORE</a>
</section>

<section class="practice-head">
  <h2>OUR PRACTICE AREAS</h2>
  <div class="rule light"><span></span><span></span></div>
  <p>Lorem ipsum dolor sit amet, consectetur adipiscing elit, sed do eiusmod tempor incididunt ut labore et dolore magna aliqua. Ut enim ad minim veniam, quis nostrud exercita</p>
</section>

<svg class="layer" viewBox="0 0 1200 4474">
  <defs>
    <linearGradient id="tileA" x1="0" y1="0" x2="1" y2="1"><stop offset="0" stop-color="#c9a23a"/><stop offset="1" stop-color="#1b2a3c"/></linearGradient>
    <linearGradient id="tileB" x1="0" y1="0" x2="1" y2="1"><stop offset="0" stop-color="#6f8a5a"/><stop offset="1" stop-color="#5b6573"/></linearGradient>
    <linearGradient id="tileC" x1="0" y1="0" x2="1" y2="1"><stop offset="0" stop-color="#d9a04a"/><stop offset="1" stop-color="#a3252d"/></linearGradient>
    <linearGradient id="tileD" x1="0" y1="0" x2="1" y2="1"><stop offset="0" stop-color="#9fb3c8"/><stop offset="1" stop-color="#33506e"/></linearGradient>
    <linearGradient id="tileE" x1="0" y1="0" x2="1" y2="1"><stop offset="0" stop-color="#2a3b55"/><stop offset="1" stop-color="#101722"/></linearGradient>
  </defs>
  <g stroke="#7BADD7" stroke-width="4">
    <polygon role="img" aria-label="Injured construction worker being helped" points="292,1440 428,1586 292,1732 156,1586" fill="url(#tileA)"/>
    <polygon role="img" aria-label="Car accident scene" points="599,1440 735,1586 599,1732 463,1586" fill="url(#tileB)"/>
    <polygon role="img" aria-label="Pile of colourful pills" points="907,1440 1043,1586 907,1732 771,1586" fill="url(#tileC)"/>
    <polygon role="img" aria-label="Surgeons in an operating room" points="455,1666 591,1812 455,1958 319,1812" fill="url(#tileD)"/>
    <polygon role="img" aria-label="Medical device monitor" points="756,1666 892,1812 756,1958 620,1812" fill="url(#tileE)"/>
  </g>
</svg>
<div class="area-label" style="left:192px;top:1560px">Personal<br>Injury</div>
<div class="area-label" style="left:499px;top:1560px">Car &amp; Truck<br>Accident</div>
<div class="area-label" style="left:807px;top:1560px">Dangerous<br>Drugs</div>
<div class="area-label" style="left:355px;top:1786px">Medical<br>Malpractice</div>
<div class="area-label" style="left:656px;top:1788px">Deffective<br>Device</div>

<svg class="layer" viewBox="0 0 1200 4474" aria-hidden="true">
  <polyline points="0,2018 596,2152 596,2672 0,2788" fill="none" stroke="#1d9bf0" stroke-width="6"/>
</svg>
<div class="comp-photo" role="img" aria-label="Client handing documents to a lawyer across a desk"></div>
<section class="comp">
  <h2 class="heading">GET &nbsp;MEANINGFUL COMPENSATION</h2>
  <div class="rule"><span></span><span></span></div>
  <p class="copy">Lorem ipsum dolor sit amet, consectetur adipiscing elit, sed do eiusmod tempor incididunt ut labore et dolore magna aliqua. Ut enim ad minim veniam, quis nostrud exercitation ullamco laboris nisi ut aliquip ex ea commodo consequat. Duis aute irure dolor in reprehenderit in voluptate velit esse cillum dolore eu fugiat nulla pariatur. Excepteur sint occaecat cupidatat non proident, sunt in culpa qui officia deserunt mollit anim id est laborum.Sed ut perspiciatis unde omnis iste natus error sit voluptatem odit aut fugit, sedratione voluptatem sequi nesciunt.</p>
  <a class="btn" href="#">READ MORE</a>
</section>

<section class="clients">
  <h2>OUR HAPPY CLIENTS</h2>
  <svg width="52" height="44" viewBox="0 0 52 44" style="margin-top:22px" aria-hidden="true">
    <path d="M22 4C10 8 2 16 2 28a8 8 0 1 0 16 0 8 8 0 0 0-8-8c1-6 6-10 12-12z M50 4C38 8 30 16 30 28a8 8 0 1 0 16 0 8 8 0 0 0-8-8c1-6 6-10 12-12z" fill="#fff"/>
  </svg>
  <p class="quote-text">Lorem ipsum dolor sit amet, consectetur adipiscing elit, sed do eiusmod tempor incididunt ut labore et dolore magna aliqua. Ut enim ad minim veniam, quis nostrud exercitation ullamco laboris nisi ut aliquip ex ea commodo consequat. Duis aute irure dolor in reprehenderit in voluptate velit esse cnulla pariatur.</p>
</section>
<svg class="layer" viewBox="0 0 1200 4474">
  <polygon role="img" aria-label="Client portrait" points="258,3127 365,3254 151,3254" fill="#e9eef3"/>
  <polygon role="img" aria-label="Client portrait" points="313,3164 530,3164 421,3292" fill="#d8b6c8"/>
  <polygon role="img" aria-label="Client portrait" points="603,3127 712,3254 495,3254" fill="#cde3ef"/>
  <polygon role="img" aria-label="Client portrait" points="665,3164 882,3164 773,3292" fill="#b8bcc2"/>
  <polygon role="img" aria-label="Client portrait" points="945,3127 1051,3254 839,3254" fill="#f1f3f5"/>
</svg>
<div class="client-name">- MARINA HOLT</div>
<div class="client-role">Lorem Ipsum</div>
<div class="dots"><span></span><span></span><span></span><span></span><span></span></div>

<section class="contact">
  <h2 class="heading">CONTACT US</h2>
  <div class="rule"><span></span><span></span></div>
</section>
<div class="field" style="left:150px;top:3680px;width:218px;height:34px">First Name</div>
<div class="field" style="left:380px;top:3680px;width:218px;height:34px">Second Name</div>
<div class="field" style="left:150px;top:3732px;width:218px;height:34px">Phone Number</div>
<div class="field" style="left:380px;top:3732px;width:218px;height:34px">Email Address</div>
<div class="field" style="left:150px;top:3785px;width:448px;height:78px">Message</div>
<a class="btn submit" href="#">SUBMIT</a>

<aside class="touch">
  <div class="touch-photo" role="img" aria-label="Smiling attorney with arms crossed"></div>
  <h2>GET IN TOUCH</h2>
  <div class="rule light"><span></span><span></span></div>
  <div class="contact-item" style="top:175px">
    <span class="icon"><svg width="16" height="20" viewBox="0 0 16 20"><path d="M8 0a8 8 0 0 0-8 8c0 6 8 12 8 12s8-6 8-12a8 8 0 0 0-8-8zm0 11a3 3 0 1 1 0-6 3 3 0 0 1 0 6z" fill="#0b63c9"/></svg></span>
    <div><b>Location</b><small>123 ipsum dolor sit amet, cons<br>adipiscing elit</small></div>
  </div>
  <div class="contact-item" style="top:272px">
    <span class="icon"><svg width="18" height="18" viewBox="0 0 24 24"><path d="M6.6 10.8a15 15 0 0 0 6.6 6.6l2.2-2.2a1 1 0 0 1 1-.25 11 11 0 0 0 3.6.6 1 1 0 0 1 1 1V20a1 1 0 0 1-1 1A17 17 0 0 1 3 4a1 1 0 0 1 1-1h3.5a1 1 0 0 1 1 1c0 1.25.2 2.45.6 3.6a1 1 0 0 1-.25 1z" fill="#0b63c9"/></svg></span>
    <div><b>Call Us</b><small>888 888 8888</small></div>
  </div>
  <div class="contact-item" style="top:350px">
    <span class="icon"><svg width="18" height="14" viewBox="0 0 18 14"><rect width="18" height="14" rx="2" fill="#0b63c9"/><path d="M1 2l8 6 8-6" stroke="#fff" stroke-width="1.6" fill="none"/></svg></span>
    <div><b>Email</b><small>info@northgatelaw.com</small></div>
  </div>
</aside>

<footer>
  <div class="footer-name">NORTHGATE LAW</div>
  <nav class="footer-nav"><a href="#">Home</a><a href="#">Our Firm</a><a href="#">Practice Areas</a><a href="#">Testimonials</a><a href="#">Blog</a><a href="#">Contact</a></nav>
  <div class="social"><span></span><span></span><span></span></div>
  <div class="copyright">COPYRIGHT © 2023 NORTHGATE LAW, ALL RIGHTS RESERVED</div>
</footer>

</body>
</html>
```